Catering Menu Package

I currently have a complete menu package, which we have redesigned as far as content, now I need to it put together in a catalog type format. It is essentially 10-12 pages in length, and will be sent for print production. Upon receiving a final edit
Updates

I have added an example gif to the project.

I did this free hand this basically what I am looking for. please change text and type to whatever you think would look best. This is a total rough design so, feel free to change any and everything. The text for the page is on the word documents. If you need more images let me know I am in the process of getting as many images uploaded for your use.

Reason: I figured we got a late jump with questions, so i am extending a few days .

Target Market(s)

The target market is business who wish to have catered luncheons, breakfasts , meetings

Industry/Entity Type

Catering

Requirements
Must have
• I have attached a copy of the text that what we want in the package, our logo, and i have also attached a catering package of another company to give you an idea what the finished product will be
Should not have
• It should not look identical to the example catering packages, these are for some inspiration we want our own design with the same type of look and feel

```html
<!DOCTYPE html>
<html lang="en">
<head>
<meta charset="utf-8">
<title>Light Breakfast – Harford Meadow Caterers</title>
<link rel="stylesheet" href="https://fonts.googleapis.com/css2?family=Delius&family=Great+Vibes&display=swap">
<style>
  :root {
    --paper: #ffffff;
    --paper-shade: #ecebec;
    --ink: #4a3b33;
    --heading-rose: #a9469c;
    --heading-plum: #6f3f95;
    --note-ink: #5a5552;
    --band-light: #f4efef;
    --band-dark: #d8cccb;
    --brand-square: #857c78;
    --title-ink: #3e3a3a;
  }
  * { margin: 0; padding: 0; box-sizing: border-box; }
  html, body { width: 1200px; height: 927px; overflow: hidden; }
  body {
    position: relative;
    background: radial-gradient(ellipse at 85% 20%, var(--paper-shade) 0%, var(--paper) 55%);
    font-family: "Delius", "Comic Sans MS", cursive;
    color: var(--ink);
  }
  .fruit-bowl-photo {
    position: absolute; left: -10px; top: -12px; width: 180px; height: 178px;
    border-radius: 50%;
    background: radial-gradient(circle at 45% 45%, #f4c84a 0%, #e0733a 35%, #8bb63f 62%, #d9b23c 80%, #c99a2c 100%);
  }
  .page-title {
    position: absolute; left: 210px; top: 38px;
    font-family: "Great Vibes", cursive; font-size: 58px; font-weight: 400;
    color: var(--title-ink);
    text-shadow: 2px 3px 3px rgba(0,0,0,0.25);
  }
  .menu-column { position: absolute; top: 154px; }
  .menu-column.left { left: 197px; width: 450px; }
  .menu-column.right { left: 697px; width: 470px; }
  .menu-item { margin-bottom: 22px; }
  .menu-item h2 {
    font-size: 19px; font-weight: 400; line-height: 26px;
    color: var(--heading-rose); -webkit-text-stroke: 0.4px var(--heading-rose);
  }
  .right .menu-item h2 { color: var(--heading-plum); -webkit-text-stroke: 0.4px var(--heading-plum); }
  .menu-item p { font-size: 15px; line-height: 24px; }
  .add-on { font-size: 15px; line-height: 24px; margin: -2px 0 22px; }
  .add-on .price { margin-left: 22px; }
  .pricing-note {
    position: absolute; left: 197px; top: 522px;
    font-family: Arial, Helvetica, sans-serif; font-style: italic;
    font-size: 14px; line-height: 17px; color: var(--note-ink);
  }
  .photo { position: absolute; }
  .photo.hot-breakfast {
    left: 618px; top: 635px; width: 191px; height: 127px;
    background: linear-gradient(160deg, #c9b8a8 0%, #e9c240 40%, #a2452e 70%, #f2e8dc 100%);
  }
  .photo.tea-table {
    left: 821px; top: 560px; width: 149px; height: 201px;
    background: linear-gradient(170deg, #e5b64b 0%, #c7873a 40%, #a73b2a 65%, #6a5a8a 100%);
  }
  .photo.bagel {
    left: 982px; top: 571px; width: 194px; height: 180px; border-radius: 8px;
    background: radial-gradient(ellipse at 50% 50%, #f2e2a8 0%, #c9a071 40%, #8f7a66 75%, #d6d2ce 100%);
  }
  .brand-band {
    position: absolute; left: 0; top: 780px; width: 1200px; height: 147px;
    background: linear-gradient(90deg, var(--band-light) 0%, var(--band-dark) 45%, var(--band-light) 100%);
  }
  .brand-mark {
    position: absolute; left: 40px; top: 818px; width: 70px; height: 70px;
    background: var(--brand-square);
  }
  .brand-name {
    position: absolute; left: 134px; top: 828px;
    font-family: "Delius", "Comic Sans MS", cursive; font-weight: 400;
    font-size: 42px; line-height: 50px;
    color: var(--ink); white-space: nowrap;
  }
</style>
</head>
<body>
  <div class="fruit-bowl-photo" role="img" aria-label="Photo of a bowl of fresh fruit salad"></div>
  <h1 class="page-title">Light Breakfast</h1>

  <section class="menu-column left">
    <article class="menu-item">
      <h2>Quick and Easy</h2>
      <p>French Pastry, a Fresh Baked Gourmet Muffin, &amp; Whole<br>Fresh Fruit (featuring Local Apples &amp; Peaches, California<br>Oranges, or Bananas).</p>
    </article>
    <article class="menu-item">
      <h2>Fast Farmhouse</h2>
      <p>Fresh baked Breakfast Bread &amp; Buttery Biscuits, Whipped<br>Butter &amp; House-made Strawberry Jam (featuring Local<br>Apples &amp; Peaches, California Oranges, or Bananas).</p>
    </article>
    <article class="menu-item">
      <h2>Light and Lean</h2>
      <p>Individual Yogurt, Fresh Fruit &amp; Berry Cups &amp; House-made<br>Granola.</p>
    </article>
  </section>

  <section class="menu-column right">
    <article class="menu-item">
      <h2>New Yorker</h2>
      <p>Brooklyn Bagel, Whipped Cream Cheese, House-made<br>Strawberry Jam &amp; Local Fruit Jellies, Whipped Butter, &amp; Whole<br>Fresh Fruit (featuring Local Apples &amp; Peaches, California<br>Oranges, or Bananas).</p>
    </article>
    <p class="add-on">Add Smoked Salmon <span class="price">$6.66</span></p>
    <article class="menu-item">
      <h2>City Farmhouse</h2>
      <p>Fresh Baked Buttery Biscuits, Gourmet Muffins &amp; Breakfast<br>Breads, Brooklyn Bagels, Whole Fresh Fruit (featuring Local<br>Apples &amp; Peaches, California Oranges, or Bananas), Whipped<br>Butter &amp; Cream Cheese, House-made Strawberry Jam &amp;<br>Local Fruit Jellies.</p>
    </article>
  </section>

  <p class="pricing-note">All Prices are per Person, with a 10 person minimum order per item chosen.<br>Local Products used when available &amp; in season</p>

  <div class="photo hot-breakfast" role="img" aria-label="Photo of scrambled eggs, bacon and sausages"></div>
  <div class="photo tea-table" role="img" aria-label="Photo of a breakfast table with teapot, jam and biscuits"></div>
  <div class="photo bagel" role="img" aria-label="Photo of a sesame bagel with butter"></div>

  <footer>
    <div class="brand-band"></div>
    <div class="brand-mark"></div>
    <p class="brand-name">Harford Meadow Caterers</p>
  </footer>
</body>
</html>
```